Zielgruppe
wir sind ein ambulanter Pflegedienst
Aufgabenstellung
Es soll ein Flyer entworfen werden.
Im Vordergrund steht die Behandlungspflege. Patienten sollen darauf aufmerksam gemacht werden, dass wir Insulininjektionen übernehmen und Kompressionsstrümpfe anziehen, wenn der Hausarzt dafür eine Verordnung ausstellt.
Im Vordergrund steht die Insulininjektion und das an und ausziehen der Kompressionsstrümpfe.
Falls die Patienten es nicht mehr alleine schaffen, springt der Pflegedienst ein.
Wichtig ist, dass das Pflegegeld nicht gekürzt wird, da dies eine Leistung der Krankenkasse ist.
Daten des Pflegedienstes:
Pflegehaus Lindental
Birkenweg 27
18057 Rostock
Tel 0800 4417236
www.Pflegehaus-Lindental.de
info@Pflegehaus-Lindental.de

```html
<!DOCTYPE html>
<html lang="de">
<head>
<meta charset="utf-8">
<title>Pflegehaus Lindental – Flyer Behandlungspflege</title>
<link href="https://fonts.googleapis.com/css2?family=Arimo:ital,wght@0,400;0,700;1,300;1,400;1,700&display=swap" rel="stylesheet">
<style>
  :root {
    --green: #6fb23a;
    --blue: #0d4f9a;
    --band-blue: #0b5199;
    --orange: #f0882a;
    --white: #ffffff;
    --stage: #5e5a5b;
    --teal: #22b9c8;
  }
  * { margin: 0; padding: 0; box-sizing: border-box; }
  html, body {
    width: 1200px; height: 900px; overflow: hidden;
    background: var(--stage);
    font-family: "Arimo", Arial, sans-serif;
  }
  .flyer {
    position: absolute; left: 0; top: 24px;
    width: 1200px; height: 851px;
    background: var(--white);
    overflow: hidden;
  }
  .brand {
    position: absolute; left: 50px; top: 17px; width: 230px;
    display: flex; flex-direction: column; align-items: center;
  }
  .brand-dot {
    width: 157px; height: 157px; border-radius: 50%;
    border: 8px solid var(--blue);
  }
  .brand-name {
    margin-top: 10px; font-weight: 700; font-size: 28px;
    color: var(--green); text-align: center; line-height: 1.1;
  }
  .photo { position: absolute; }
  .photo-nurse {
    left: 13px; top: 276px; width: 280px; height: 492px;
    background: linear-gradient(180deg, #ffffff 0%, #f3e2d4 22%, #5cd0da 45%, var(--teal) 80%, #f2f2f2 100%);
    border-radius: 110px 110px 0 0;
  }
  .photo-framed { border: 3px solid var(--orange); border-radius: 7px; }
  .photo-injection {
    left: 844px; top: 285px; width: 273px; height: 185px;
    background: linear-gradient(180deg, #f4f4f4 0%, #d8a683 40%, #c98e6a 70%, #e8e0cf 100%);
  }
  .photo-socks {
    left: 735px; top: 514px; width: 272px; height: 184px;
    background: radial-gradient(ellipse at 50% 50%, #3a3a3a 0%, #4a4a4a 35%, #ffffff 70%);
  }
  .headline {
    position: absolute; left: 346px; top: 70px;
    font-size: 80px; font-weight: 700; font-style: italic;
    color: var(--green); letter-spacing: 1px; line-height: 1;
    white-space: nowrap;
  }
  .swoosh { position: absolute; left: 306px; top: 142px; }
  .intro {
    position: absolute; left: 307px; top: 240px;
    font-size: 28px; font-weight: 700; color: var(--blue); line-height: 29px;
    white-space: nowrap;
  }
  .intro span { display: block; }
  .intro span + span { padding-left: 3px; }
  .services {
    position: absolute; left: 307px; top: 317px;
    list-style: none; font-size: 30px; font-weight: 700;
    color: var(--green); line-height: 29px; white-space: nowrap;
  }
  .services li { padding-left: 14px; position: relative; }
  .services li::before { content: "•"; position: absolute; left: 0; font-size: 20px; }
  .services li.gap { margin-top: 6px; }
  .services .cont { display: block; margin-top: 3px; }
  .cost {
    position: absolute; left: 363px; top: 458px;
    font-size: 38px; font-weight: 700; font-style: italic;
    color: var(--blue); line-height: 45px; white-space: nowrap;
  }
  .cost span { display: block; }
  .cost span:first-child { padding-left: 7px; }
  .contact {
    position: absolute; left: 317px; top: 610px;
    font-style: italic; font-weight: 300; color: var(--green);
    font-size: 21px; line-height: 28px; white-space: nowrap;
  }
  .contact .name { font-size: 27px; font-weight: 400; line-height: 32px; padding-left: 7px; }
  .contact .addr { padding-left: 5px; }
  .callout {
    position: absolute; left: 0; top: 769px; width: 1200px; height: 82px;
    background: var(--band-blue);
    display: flex; align-items: center; padding-left: 16px;
    font-weight: 700; color: var(--white); white-space: nowrap;
  }
  .callout .label { font-size: 35px; }
  .callout .phone { font-size: 45px; color: var(--green); margin-left: 22px; }
  .callout .free { font-size: 34px; margin-left: 12px; }
</style>
</head>
<body>
  <main class="flyer">
    <div class="brand">
      <div class="brand-dot"></div>
      <div class="brand-name">Pflegehaus Lindental</div>
    </div>

    <div class="photo photo-nurse" role="img" aria-label="Foto einer lächelnden Pflegerin in türkisfarbener Dienstkleidung mit erhobenem Daumen"></div>
    <div class="photo photo-framed photo-injection" role="img" aria-label="Foto einer Insulininjektion mit Spritze in die Bauchhaut"></div>
    <div class="photo photo-framed photo-socks" role="img" aria-label="Foto eines Paars schwarzer Kompressionsstrümpfe"></div>

    <h1 class="headline">Wir helfen Ihnen</h1>
    <svg class="swoosh" width="680" height="26" viewBox="0 0 680 26" aria-hidden="true">
      <path d="M2 16 C 120 6, 420 2, 678 4 C 560 16, 300 24, 4 23 Z" fill="var(--orange)"/>
    </svg>

    <p class="intro">
      <span>Unser abulantes Pflegeteam</span>
      <span>übernimmt auf ärtzliche Verordnung</span>
    </p>

    <ul class="services">
      <li>Insulininjektionen</li>
      <li>Blutzuckerkontrollen</li>
      <li class="gap">An und Ausziehen<span class="cont">von Kompressionsstrümpfen</span></li>
    </ul>

    <p class="cost">
      <span>Die Kosten trägt die</span>
      <span>Krankenkasse</span>
    </p>

    <address class="contact">
      <div class="name">Pflegehaus Lindental</div>
      <div class="addr">Birkenweg 27</div>
      <div class="addr">18057 Rostock</div>
      <div>info@Pflegehaus-Lindental.de</div>
      <div>www.Pflegehaus-Lindental.de</div>
    </address>

    <footer class="callout">
      <span class="label">Infomieren sich sich kostenlos unter:</span>
      <span class="phone">0800 441 72 36</span>
      <span class="free">(kostenfrei)</span>
    </footer>
  </main>
</body>
</html>
```